K9 Orbit needs a business card designed

We need a business card designed for K9 Orbit, an expansion of K9 Systems Pty Ltd (www.k9systems.com.au)

We provide high quality professional services for the Australian space industry. Our clients include the Southern Launch Bureau and companies working in the space industry. We identify people with space related skills both locally and internationally who are then contracted by clients to create products and support space launch activities.

Colours to be used:
- Navy blue #000080
- Rocket metallic #8A7F8D
- Platinum #E5E4E2
- Black #000000
- White #FFFFFF

*Front of the card*
I have attached our K9 Orbit logo, which needs to be the main item on the card. The 'Space' text should be placed to the right of the 'K9' part rather than below, similar to the attached K9 Systems card, which this card should match.

If subtext is included, however, it should read ‘Labour Hire • Consultancy • Project Delivery’ rather than the ‘Design • Build • Test • Maintain’ of the K9 Systems card.

A black background (rather than blue background in the K9 Systems card) might be good, with a white pattern as in the K9 Systems card. If colour is used, the logo should be in its standard colours (as provided for the K9 Orbit logo).

*Back of the card*
Include a smaller K9 Orbit logo on the back.

We need the following details for K9 Orbit personnel (as a template for entry):
- Name
- Company Position
- Mobile Number
- Email
- Office Address
- Include the K9 Orbit website: www.k9orbit.com.au

Overall, we'd like to see a design that communicates the adventure of space, professional integrity, and customer service. We look forward to seeing what you can come up with.

Target Market(s)

We provide high quality professional services for the Australian space industry. Our clients include the Southern Launch Bureau and companies working in the space industry.

Contact Information for Business Card

- Name
- Company Position
- Mobile Number
- Email
- Office Address

Requirements
Must have
• See project description.

```html
<!DOCTYPE html>
<html lang="en">
<head>
<meta charset="utf-8">
<title>K9 Orbit Business Card</title>
<link href="https://fonts.googleapis.com/css2?family=Arimo:wght@400;700&family=Montserrat:wght@600&display=swap" rel="stylesheet">
<style>
  :root {
    --backdrop: #1d1d1f;
    --navy: #25237a;
    --navy-deep: #1c1a66;
    --navy-light: #3a3896;
    --white: #ffffff;
    --soft: rgba(255,255,255,0.07);
  }
  * { margin: 0; padding: 0; box-sizing: border-box; }
  html, body { width: 1200px; height: 900px; overflow: hidden; }
  body { background: var(--backdrop); font-family: "Arimo", Arial, sans-serif; color: var(--white); position: relative; }

  .card {
    position: absolute; width: 580px; height: 330px; border-radius: 22px; overflow: hidden;
    background: linear-gradient(135deg, var(--navy-deep) 0%, var(--navy) 55%, var(--navy-light) 100%);
  }
  .card-front { left: 70px; top: 80px; }
  .card-back { left: 550px; top: 490px; }

  .bg-disc { position: absolute; left: 40px; top: 40px; width: 300px; height: 300px; border-radius: 50%; background: var(--soft); }

  .brand { position: absolute; display: flex; align-items: center; gap: 12px; font-family: "Montserrat", Arial, sans-serif; font-weight: 600; color: var(--white); letter-spacing: 3px; white-space: nowrap; }
  .brand-dot { width: 14px; height: 14px; border-radius: 50%; background: var(--white); flex: none; }
  .card-front .brand { left: 40px; top: 138px; font-size: 40px; }
  .card-back .brand { right: 40px; top: 50px; font-size: 32px; }

  .divider-v { position: absolute; left: 360px; top: 90px; width: 1px; height: 150px; background: rgba(255,255,255,0.7); }
  .services { position: absolute; left: 385px; top: 128px; list-style: none; font-size: 17px; line-height: 26px; }
  .services li::before { content: "• "; }

  .person { position: absolute; left: 40px; top: 134px; }
  .person-name { font-weight: 700; font-size: 24px; letter-spacing: 0.5px; white-space: nowrap; }
  .person-role { font-size: 17px; margin-top: 4px; }
  .divider-h { position: absolute; left: 270px; right: 40px; top: 160px; height: 1px; background: rgba(255,255,255,0.85); }
  .address { position: absolute; right: 40px; top: 172px; text-align: right; font-size: 15px; line-height: 19px; }
  .contact-rule { position: absolute; left: 40px; width: 230px; top: 202px; height: 1px; background: rgba(255,255,255,0.85); }
  .contacts { position: absolute; left: 40px; top: 212px; list-style: none; font-size: 18px; }
  .contacts li { display: flex; align-items: center; gap: 10px; height: 28px; white-space: nowrap; }
  .contacts svg { width: 20px; height: 20px; flex: none; }
</style>
</head>
<body>
  <section class="card card-front">
    <div class="bg-disc"></div>
    <div class="brand"><span class="brand-dot"></span>K9 ORBIT</div>
    <div class="divider-v"></div>
    <ul class="services">
      <li>Labour Hire</li>
      <li>Consultancy</li>
      <li>Project Delivery</li>
    </ul>
  </section>

  <section class="card card-back">
    <div class="brand"><span class="brand-dot"></span>K9 ORBIT</div>
    <div class="person">
      <div class="person-name">DANIEL HARPER</div>
      <div class="person-role">Manager</div>
    </div>
    <div class="divider-h"></div>
    <div class="address">Your address, city<br>state, ZIP 0000</div>
    <div class="contact-rule"></div>
    <ul class="contacts">
      <li><svg viewBox="0 0 20 20"><rect width="20" height="20" rx="4" fill="#fff"/><path d="M6 4l3 3-1.5 1.5a8 8 0 0 0 4 4L13 11l3 3-2 2C9 16 4 11 4 6z" fill="#25237a"/></svg>123-555-0142</li>
      <li><svg viewBox="0 0 20 20"><rect width="20" height="20" rx="4" fill="#fff"/><rect x="3.5" y="5.5" width="13" height="9" fill="none" stroke="#25237a" stroke-width="1.5"/><path d="M3.5 5.5l6.5 5 6.5-5" fill="none" stroke="#25237a" stroke-width="1.5"/></svg>info@k9orbit.com.au</li>
      <li><svg viewBox="0 0 20 20"><rect width="20" height="20" rx="4" fill="#fff"/><circle cx="10" cy="10" r="6" fill="none" stroke="#25237a" stroke-width="1.5"/><path d="M4 10h12M10 4c-3 3-3 9 0 12M10 4c3 3 3 9 0 12" fill="none" stroke="#25237a" stroke-width="1.2"/></svg>www.k9orbit.com.au</li>
    </ul>
  </section>
</body>
</html>
```